VBN Line Card

We are looking for a line card to leave with potential customers.
Logo on top

VBN is a Colorado-based business specializing in demolition, materials management, hazardous materials management, and trucking & hauling. What differentiates VBN is our breadth of experience in upcycling much of reusable debris from the demolition process for reuse on existing projects or recycling the material for later use on other projects.

We offer an end-to-end client experience that includes seamless communication, budgeting, staffing, on-site organization, and solid, quality work every time.

Trucking and Hauling Equipment:
30 yd End Dump
Steel Side Scrap Trailer
90 yr End Dump
Flatbeds
70 Ton Lowboy Trailer 2-3-2 combo

Gordon Ellery
President
720-463-9170
gellery@vbnmetalworks.com

I'd like it to be easy to read, but look modern

Target Market(s)

General Contractors

Industry/Entity Type

Construction

Colors
EB3D1F
EC4F4E
F09395
F8D3D4
FCEDEE

Requirements
Must have
• Our colors and red and gun metal gray

```html
<!DOCTYPE html>
<html lang="en">
<head>
<meta charset="UTF-8">
<title>VBN Line Card</title>
<link href="https://fonts.googleapis.com/css2?family=Roboto:ital,wght@0,700;1,500;1,700;1,900&family=Raleway:wght@400;500&display=swap" rel="stylesheet">
<style>
  :root {
    --red: #EB3D1F;
    --red-deep: #C8202A;
    --red-soft: #EC4F4E;
    --pink: #F09395;
    --blush: #F8D3D4;
    --mist: #FCEDEE;
    --gunmetal: #2B2D30;
    --gunmetal-dark: #141517;
    --ink: #1A1A1A;
    --white: #FFFFFF;
  }
  * { margin: 0; padding: 0; box-sizing: border-box; }
  html, body { width: 834px; height: 1200px; overflow: hidden; background: var(--white); }
  .card {
    position: relative;
    width: 834px;
    height: 1200px;
    overflow: hidden;
    background: var(--white);
    font-family: "Raleway", sans-serif;
    color: var(--ink);
  }
  .layer { position: absolute; inset: 0; }

  .brand {
    position: absolute;
    top: 40px;
    left: 250px;
    width: 400px;
    text-align: center;
    font-family: "Roboto", sans-serif;
    font-weight: 900;
    font-style: italic;
    font-size: 96px;
    letter-spacing: 16px;
    line-height: 1;
    color: var(--red);
  }

  .tagline {
    position: absolute;
    top: 168px;
    left: 30px;
    font-family: "Roboto", sans-serif;
    font-weight: 700;
    font-style: italic;
    font-size: 23px;
    line-height: 52px;
    color: var(--white);
  }

  .year-badge {
    position: absolute;
    left: 628px;
    top: 302px;
    width: 176px;
    height: 176px;
    border-radius: 50%;
    background: var(--white);
    border: 11px solid var(--red-deep);
    box-shadow: 0 0 0 4px var(--white), 0 4px 14px rgba(0,0,0,.25);
    display: flex;
    align-items: center;
    justify-content: center;
    font-family: "Roboto", sans-serif;
    font-weight: 700;
    font-style: italic;
    font-size: 56px;
    color: var(--red-deep);
  }

  .intro {
    position: absolute;
    top: 592px;
    right: 60px;
    width: 440px;
    text-align: right;
    font-size: 16.5px;
    line-height: 21.5px;
  }
  .intro strong { font-weight: 500; color: var(--red-deep); }

  .services-title {
    position: absolute;
    top: 760px;
    left: 372px;
    font-family: "Roboto", sans-serif;
    font-weight: 700;
    font-style: italic;
    font-size: 28px;
    color: var(--red-deep);
  }
  .services-list {
    position: absolute;
    top: 822px;
    left: 0;
    list-style: none;
    font-size: 17.5px;
    line-height: 22.5px;
  }
  .services-list li { white-space: nowrap; }

  .president-heading {
    position: absolute;
    top: 998px;
    left: 200px;
    font-family: "Roboto", sans-serif;
    font-weight: 700;
    font-style: italic;
    font-size: 27px;
    line-height: 44px;
    color: var(--white);
  }

  .contact {
    position: absolute;
    top: 1054px;
    left: 0;
    list-style: none;
    font-family: "Roboto", sans-serif;
    font-style: italic;
    font-weight: 500;
    font-size: 25px;
    line-height: 32.5px;
  }
  .contact li { white-space: nowrap; }

  .sign-off {
    position: absolute;
    top: 1000px;
    right: 24px;
    width: 220px;
    text-align: right;
    font-family: "Roboto", sans-serif;
    font-weight: 700;
    font-style: italic;
    font-size: 20px;
    line-height: 26px;
    color: var(--white);
  }

  .social {
    position: absolute;
    top: 1120px;
    left: 552px;
    display: flex;
    gap: 22px;
    list-style: none;
  }
  .social li {
    width: 72px;
    display: flex;
    flex-direction: column;
    align-items: center;
    gap: 10px;
  }
  .social-dot {
    width: 42px;
    height: 42px;
    border-radius: 50%;
    background: var(--red-deep);
  }
  .social-label {
    font-family: "Roboto", sans-serif;
    font-size: 10px;
    font-weight: 700;
    color: var(--white);
    white-space: nowrap;
  }
</style>
</head>
<body>
<div class="card">

  <svg class="layer" width="834" height="1200" viewBox="0 0 834 1200" aria-hidden="true">
    <defs>
      <linearGradient id="bandRed" x1="0" y1="0" x2="1" y2="0">
        <stop offset="0" stop-color="#EB3D1F"/>
        <stop offset="1" stop-color="#B81C26"/>
      </linearGradient>
      <linearGradient id="gunmetalFade" x1="0" y1="0" x2="1" y2="1">
        <stop offset="0" stop-color="#3A3C40"/>
        <stop offset="1" stop-color="#0E0F10"/>
      </linearGradient>
      <linearGradient id="sceneTone" x1="0" y1="0" x2="0.7" y2="1">
        <stop offset="0" stop-color="#6B6F76"/>
        <stop offset="0.55" stop-color="#44474D"/>
        <stop offset="1" stop-color="#26282C"/>
      </linearGradient>
    </defs>
  </svg>

  <svg class="layer" width="834" height="1200" viewBox="0 0 834 1200" role="img" aria-label="Illustration of a city construction site with an excavator, a cement mixer truck, a loader and traffic cones beside tall glass buildings">
    <polygon points="250,0 700,0 700,150 834,150 834,165 340,576 130,990 0,990 0,275" fill="url(#sceneTone)"/>
  </svg>

  <svg class="layer" width="834" height="1200" viewBox="0 0 834 1200" aria-hidden="true">
    <polygon points="62,0 250,0 0,275 0,70" fill="var(--gunmetal-dark)"/>
    <polygon points="300,30 700,30 700,150 240,150" fill="var(--white)"/>
    <polygon points="0,168 720,168 700,220 0,220" fill="url(#bandRed)"/>
    <polygon points="405,520 834,520 834,576 340,576" fill="url(#bandRed)"/>
    <polygon points="834,660 834,1200 510,1200 650,985" fill="url(#gunmetalFade)"/>
    <polygon points="0,998 650,998 618,1042 30,1042" fill="url(#bandRed)"/>
    <polygon points="0,1042 30,1042 0,1070" fill="var(--red-deep)"/>
    <polygon points="0,990 120,1110 60,1110 0,1050" fill="var(--gunmetal-dark)"/>
  </svg>

  <div class="brand">VBN</div>

  <p class="tagline">Construction Excellence - Your Partner in Building Dreams!</p>

  <div class="year-badge">2024</div>

  <p class="intro">
    <strong>Colorado-based demolition, materials and hazardous<br>
    materials management, and trucking &amp; hauling &ndash;<br>
    upcycling reusable debris for reuse and recycling.</strong><br>
    Are you looking for a construction partner that<br>
    prioritizes seamless communication, efficient budget-<br>
    ing, skilled staffing, organized on-site management,<br>
    and top-notch quality work every time?
  </p>

  <h2 class="services-title">Our Services</h2>
  <ul class="services-list">
    <li style="padding-left:325px">Trucking and Hauling Equipment:</li>
    <li style="padding-left:310px">30 yd End Dump</li>
    <li style="padding-left:296px">Steel Side Scrap Trailer</li>
    <li style="padding-left:282px">90 yr End Dump</li>
    <li style="padding-left:267px">Flatbeds</li>
    <li style="padding-left:252px">70 Ton Lowboy Trailer 2-3-2 combo</li>
  </ul>

  <h2 class="president-heading">Meet Our President:</h2>
  <ul class="contact">
    <li style="padding-left:172px">Gordon Ellery</li>
    <li style="padding-left:152px">President</li>
    <li style="padding-left:130px">720-463-9170</li>
    <li style="padding-left:108px">gellery@vbnmetalworks.com</li>
  </ul>

  <p class="sign-off">DEMOLITION &amp;<br>HAULING EXPERTS</p>

  <ul class="social">
    <li><span class="social-dot"></span><span class="social-label">FOLLOW US</span></li>
    <li><span class="social-dot"></span><span class="social-label">SHARE</span></li>
    <li><span class="social-dot"></span><span class="social-label">CONNECT</span></li>
  </ul>

</div>
</body>
</html>
```